Business Cards, Stationary, Envelopes, Email Signature for new Wellness Practice
Fernleaf Wellcraft
Business Cards, Stationary, Envelopes, Email Signature for new Wellness Practice - Massage Therapy
Creative Brief
Bright & Fun-filled
Danica Vorhees CMT
CranioSacral & Massage Therapist
31867 Orchard Ave, Suite 512 Larkmont Cove, OR 97409
danica@fernleafwellcraft.example
www.fernleafwellcraft.example
CMT #57364, TOVERB #62158
Include: Tune in to Fernleaf Wellcraft on (insert icons) facebook, twitter, linkedin Mossgrove CST profile http://www.quelto.example/DanicaVorhees/ Please incorporate the attached brand image into the design. My first idea is to use the brand image as the background for the card and knock out the logo and text. Please feel free to take it from there. I love the way the logo looks knocked out. I also love the way the logo looks with the bird a different color, but it has to be used in the right context or else it looks distracting.
Give yourself time to know who you are, to become all that already are. My Next Appointments Are: Day:_____ Date:______ Time:_____ Day:_____ Date:______ Time:_____ Day:_____ Date:______ Time:_____ Day:_____ Date:______ Time:_____ Day:_____ Date:______ Time:_____ If you are not able to keep you appointment, please call, text or email at least 24 hours in advance.

```html
<!DOCTYPE html>
<html lang="en">
<head>
<meta charset="utf-8">
<title>Fernleaf Wellcraft – Business Card</title>
<link rel="stylesheet" href="https://fonts.googleapis.com/css2?family=Open+Sans:ital,wght@0,400;0,600;0,700;1,400&display=swap">
<style>
  :root {
    --page-bg: #eceeef;
    --card-white: #ffffff;
    --brand-blue: #2f86c8;
    --brand-blue-deep: #1f6fae;
    --brand-green: #1f5a36;
    --logo-blue: #2a7fbf;
    --text-light: #ffffff;
  }
  * { margin: 0; padding: 0; box-sizing: border-box; }
  html, body {
    width: 1200px; height: 914px; overflow: hidden;
    background: var(--page-bg);
    font-family: "Open Sans", Arial, sans-serif;
  }
  .canvas {
    position: relative; width: 1200px; height: 914px;
  }
  .business-card {
    position: absolute; left: 100px; top: 171px;
    width: 1000px; height: 572px;
    background: var(--card-white);
    box-shadow: 0 6px 22px rgba(0,0,0,0.18);
    overflow: hidden;
  }
  .card-waves {
    position: absolute; inset: 0; width: 100%; height: 100%;
  }
  .brand-name {
    position: absolute; left: 0; right: 0; top: 118px;
    text-align: center;
    font-weight: 600; font-size: 58px; letter-spacing: 0.5px;
    color: var(--logo-blue);
  }
  .therapist {
    position: absolute; left: 0; right: 0; top: 346px;
    text-align: center; color: var(--text-light);
    padding-left: 110px;
  }
  .therapist-name { font-weight: 700; font-size: 21px; }
  .therapist-title { font-size: 16px; margin-top: 2px; }
  .address {
    position: absolute; left: 330px; top: 408px;
    color: var(--text-light); font-size: 16px; line-height: 26px;
    font-style: normal;
  }
  .contact-list {
    position: absolute; left: 590px; top: 400px;
    list-style: none; color: var(--text-light); font-size: 16px;
  }
  .contact-item { display: flex; align-items: center; height: 27px; }
  .contact-icon { width: 18px; height: 18px; margin-right: 8px; flex: none; }
</style>
</head>
<body>
<main class="canvas">
  <article class="business-card">
    <svg class="card-waves" viewBox="0 0 1000 572" preserveAspectRatio="none" aria-hidden="true">
      <path d="M0 292 C 260 336, 620 330, 1000 214 L1000 572 L0 572 Z" fill="var(--brand-green)"/>
      <path d="M0 302 C 260 344, 620 344, 1000 240 L1000 572 L0 572 Z" fill="var(--card-white)"/>
      <path d="M0 310 C 260 352, 620 354, 1000 252 L1000 572 L0 572 Z" fill="var(--brand-blue)"/>
    </svg>

    <h1 class="brand-name">Fernleaf Wellcraft</h1>

    <div class="therapist">
      <p class="therapist-name">Danica Vorhees CMT</p>
      <p class="therapist-title">CranioSacral &amp; Massage Therapist</p>
    </div>

    <address class="address">
      31867 Orchard Ave, Suite 512<br>
      Larkmont Cove, OR 97409
    </address>

    <ul class="contact-list">
      <li class="contact-item">
        <svg class="contact-icon" viewBox="0 0 20 20" aria-hidden="true">
          <circle cx="10" cy="10" r="10" fill="#fff"/>
          <path d="M6.5 5 L8.5 5 L9.3 7.6 L8 8.6 C8.7 10.2 9.8 11.3 11.4 12 L12.4 10.7 L15 11.5 L15 13.5 C15 14.2 14.4 14.8 13.7 14.7 C9.4 14.2 5.8 10.6 5.3 6.3 C5.2 5.6 5.8 5 6.5 5 Z" fill="var(--brand-blue)"/>
        </svg>
        (555) 214-0387
      </li>
      <li class="contact-item">
        <svg class="contact-icon" viewBox="0 0 20 20" aria-hidden="true">
          <circle cx="10" cy="10" r="10" fill="#fff"/>
          <rect x="5" y="6.5" width="10" height="7" fill="none" stroke="var(--brand-blue)" stroke-width="1.4"/>
          <path d="M5 6.5 L10 10.5 L15 6.5" fill="none" stroke="var(--brand-blue)" stroke-width="1.4"/>
        </svg>
        danica@fernleafwellcraft.example
      </li>
      <li class="contact-item">
        <svg class="contact-icon" viewBox="0 0 20 20" aria-hidden="true">
          <circle cx="10" cy="10" r="10" fill="#fff"/>
          <circle cx="10" cy="10" r="5" fill="none" stroke="var(--brand-blue)" stroke-width="1.3"/>
          <ellipse cx="10" cy="10" rx="2.2" ry="5" fill="none" stroke="var(--brand-blue)" stroke-width="1.1"/>
          <line x1="5" y1="10" x2="15" y2="10" stroke="var(--brand-blue)" stroke-width="1.1"/>
        </svg>
        www.fernleafwellcraft.example
      </li>
    </ul>
  </article>
</main>
</body>
</html>
```